DPM Marketing Postcard

Design a 2 Sided marketing postcard for our Real estate management caompany. Looking for a professional yet fresh look that will be printed on a 6"x9" glossy flier

Contact information is www.dunkeldmanagement-example.com dunkeldmanagement@dunkeldmail-example.com and 312-480-7193

WE are targeting small condo and town home properties to take on their administrative responsibilities of management

```html
<!DOCTYPE html>
<html lang="en">
<head>
<meta charset="utf-8">
<title>Dunkeld Property Management – Postcard Front</title>
<link rel="stylesheet" href="https://fonts.googleapis.com/css2?family=Montserrat:wght@500;600;700&display=swap">
<style>
  :root {
    --page-bg: #e9e9ec;
    --navy-deep: #16243d;
    --navy: #1d3f7e;
    --screen-blue: #1f4a94;
    --phone-frame: #2b2d31;
    --phone-bezel: #0c0c0e;
    --accent-yellow: #fbc12c;
    --panel-light: #e8e8ea;
    --ink: #111317;
    --white: #ffffff;
    --call-green: #6abd45;
  }
  * { box-sizing: border-box; margin: 0; padding: 0; }
  html, body { width: 1200px; height: 900px; overflow: hidden; }
  body {
    background: var(--page-bg);
    font-family: "Montserrat", Arial, sans-serif;
    position: relative;
  }
  .postcard {
    position: absolute;
    left: 75px; top: 96px;
    width: 1050px; height: 708px;
    overflow: hidden;
    background: var(--panel-light);
    box-shadow: 0 4px 14px rgba(0,0,0,.25);
  }
  .hero-photo {
    position: absolute;
    left: 0; top: 0; width: 1050px; height: 400px;
    background:
      radial-gradient(ellipse 260px 200px at 760px 210px, rgba(60,110,190,.55), transparent 70%),
      radial-gradient(ellipse 160px 300px at 940px 200px, rgba(220,225,235,.55), transparent 70%),
      linear-gradient(90deg, #3a4558 0%, #4c5668 35%, #1a2a4a 60%, #13223f 100%);
  }
  .lower-panel {
    position: absolute;
    left: 0; top: 400px; width: 1050px; height: 308px;
    background: linear-gradient(180deg, #dcdde1 0%, #efeff1 40%, #e4e4e6 100%);
  }
  .phone {
    position: absolute;
    left: 48px; top: 75px;
    width: 347px; height: 680px;
    background: var(--phone-bezel);
    border: 6px solid var(--phone-frame);
    border-radius: 48px;
  }
  .phone-speaker {
    position: absolute; left: 50%; top: 34px;
    width: 54px; height: 6px; margin-left: -27px;
    background: #2e3034; border-radius: 3px;
  }
  .phone-camera {
    position: absolute; left: 106px; top: 32px;
    width: 10px; height: 10px; border-radius: 50%;
    background: #2e3034;
  }
  .phone-screen {
    position: absolute;
    left: 11px; top: 78px; width: 313px; height: 600px;
    background: linear-gradient(180deg, var(--screen-blue) 0%, #1a4088 100%);
    color: var(--white);
    text-align: center;
  }
  .brand-circle {
    position: absolute; left: 86px; top: 36px;
    width: 140px; height: 140px;
    border: 8px solid var(--white); border-radius: 50%;
  }
  .brand-name {
    position: absolute; left: 0; right: 0; top: 186px;
    font-weight: 600; font-size: 34px; letter-spacing: -.3px;
  }
  .brand-sub {
    position: absolute; left: 0; right: 0; top: 230px;
    font-weight: 600; font-size: 14px;
  }
  .call-icon {
    position: absolute; left: 126px; top: 318px;
    width: 60px; height: 60px;
  }
  .phone-number {
    position: absolute; left: 0; right: 0; top: 400px;
    font-weight: 600; font-size: 35px; letter-spacing: .3px;
  }
  .web-address {
    position: absolute; left: 0; right: 0; top: 450px;
    font-weight: 700; font-size: 12.5px; color: var(--accent-yellow);
  }
  .title-band {
    position: absolute;
    left: 410px; top: 383px; width: 640px; height: 42px;
    background: var(--accent-yellow);
    border-radius: 20px 0 0 20px;
    display: flex; align-items: center; justify-content: center;
    font-weight: 700; font-size: 21.5px; color: var(--ink);
    letter-spacing: .3px;
  }
  .benefit-list {
    position: absolute;
    left: 462px; top: 440px; width: 540px;
    list-style: none;
    font-weight: 500; font-size: 13.2px; line-height: 17px; color: var(--ink);
  }
  .benefit-list li {
    position: relative; padding-left: 28px; margin-bottom: 5px;
  }
  .benefit-list li::before {
    content: "•"; position: absolute; left: 0; top: 0;
  }
</style>
</head>
<body>
  <main class="postcard">
    <div class="hero-photo" role="img" aria-label="Photo of a businessman holding a glowing network-line house above his open hand, soft blue bokeh background"></div>
    <div class="lower-panel"></div>

    <div class="phone">
      <span class="phone-camera"></span>
      <span class="phone-speaker"></span>
      <div class="phone-screen">
        <span class="brand-circle"></span>
        <div class="brand-name">Dunkeld</div>
        <div class="brand-sub">Property Management</div>
        <svg class="call-icon" viewBox="0 0 60 60" aria-hidden="true">
          <circle cx="30" cy="30" r="30" fill="var(--call-green)"/>
          <path d="M22 17c1.5-1 3-.6 3.8.8l2.4 4.3c.7 1.3.4 2.6-.7 3.5l-1.8 1.4c1.3 3 3.7 5.5 6.8 6.9l1.4-1.8c.9-1.1 2.3-1.4 3.5-.7l4.3 2.4c1.4.8 1.8 2.4.8 3.8l-1.6 2.2c-1.2 1.6-3.2 2.2-5.1 1.6C27.6 39.7 20.3 32.4 17.6 24.2c-.6-1.9 0-3.9 1.6-5.1z" fill="var(--white)"/>
        </svg>
        <div class="phone-number">312-480-7193</div>
        <div class="web-address">www.dunkeldmanagement-example.com</div>
      </div>
    </div>

    <h1 class="title-band">DUNKELD PROPERTY MANAGEMENT LLC</h1>

    <ul class="benefit-list">
      <li>Cost effective property management solution for 3-10 unit buildings</li>
      <li>Prices starting as low as $100/month</li>
      <li>Utilize our economies of scale to reduce costs across existing services (trash, insurance, maintenance, etc)</li>
      <li>Eliminate the unfair burden placed on a few owners to do all the work while others free-ride</li>
      <li>Improve communication amongst all owners and board members</li>
      <li>The association’s board of directors maintain all decision-making power</li>
      <li>Utilize our vetted service providers for prompt job completion and fair pricing</li>
    </ul>
  </main>
</body>
</html>
```